Harvest Ledger Partners Web Page

A modern and attractive Home Web Page for my rebranded Company, Harvest Ledger Partners. My existing website from my old brand is www.plumcorbelgroup.NET. I would like an up to date, modern and eye catching Home Web Page. It should entice the viewer to go further and stay on the site.
I will have my professional webmaster utilize this cover page for my redesigned site.

Target Market(s)

Privately held construction equipment rental companies looking to sell or have their business valued

Number of Pages Required

1 page

Font styles to use
Serif
Sans Serif

Colors
2f74b3
fec41b
fefbf7
faa54b
f37122
33a6d7

Requirements
Must have
• Above the fold I want to engage the customer so he stays on the sight. A call to action: "Free confidential conversation to discuss your unique situation and exit strategy or valuation of your business." Something like that in there.

Above the fold have menu and key offerings. Next section to summarize my business (again see plumcorbelgroup.NET for more info) with links to more details back in the site.
"A leading boutique M&A and Valuation advisory firm with over 30 years rental industry specific experience>
Tabs: Seller Representation
Business Valuations
Dependable Advice
Industry Articles
Industry Transactions/News
FAQ
Bottom should have key contact info

Key contact info.
Nice to have
• Logos of associations I belong to (on existing site at plumcorbelgroup.NET) (OTV and PLM only)
"Call Gus today for a free, confidential conversation regarding your unique situation and possible exit strategies."
Should not have
• Too much "busyness"

```html
<!DOCTYPE html>
<html lang="en">
<head>
<meta charset="utf-8">
<title>Harvest Ledger Partners</title>
<link href="https://fonts.googleapis.com/css2?family=Rajdhani:wght@600;700&family=Exo+2:wght@300;400;500;600&display=swap" rel="stylesheet">
<style>
:root{
  --navy:#1d2a6e;
  --blue:#2f74b3;
  --blue-deep:#2a66ad;
  --sky:#33a6d7;
  --orange:#f37122;
  --orange-deep:#ec5d1f;
  --amber:#faa54b;
  --yellow:#fec41b;
  --cream:#fefbf7;
  --text:#6b6f80;
  --white:#ffffff;
}
*{margin:0;padding:0;box-sizing:border-box}
html,body{width:1200px;height:3888px;overflow:hidden}
body{position:relative;background:var(--white);font-family:"Exo 2",sans-serif;color:var(--text)}
.abs{position:absolute}
.heading{font-family:"Rajdhani",sans-serif;font-weight:700;color:var(--navy);letter-spacing:1px}
.btn{position:absolute;display:flex;align-items:center;justify-content:center;gap:10px;background:var(--orange);color:var(--white);border-radius:40px;font-family:"Rajdhani",sans-serif;font-weight:700;font-size:15px;letter-spacing:.5px;text-decoration:none;white-space:nowrap}
.btn-arrow{width:16px;height:16px;flex:none}

/* header */
.top-rule{top:0;left:0;width:1200px;height:4px;background:var(--orange)}
.brand{top:18px;left:510px;height:58px;display:flex;align-items:center;gap:10px}
.brand-mark{width:26px;height:26px;background:var(--orange)}
.brand-name{font-family:"Rajdhani",sans-serif;font-weight:700;font-size:19px;line-height:19px;color:var(--navy);width:140px}
.call{top:24px;left:780px;display:flex;align-items:center;gap:12px;font-family:"Rajdhani",sans-serif;font-weight:700;font-size:28px;color:var(--navy)}
.nav{top:88px;left:0;width:1200px;height:45px;background:var(--blue-deep);display:flex;padding-left:136px}
.nav a{display:flex;align-items:center;padding:0 14px;color:var(--white);text-decoration:none;font-family:"Rajdhani",sans-serif;font-weight:700;font-size:14.5px;letter-spacing:.3px}
.nav a.active{background:var(--orange)}

/* hero */
.hero{top:133px;left:0;width:1200px;height:702px;background:linear-gradient(100deg,#8c98a4 0%,#a7b0b6 30%,#6a6a52 50%,#c9b23a 68%,#7e8388 85%,#c7ccd1 100%)}
.hero-shade{top:133px;left:0;width:1200px;height:702px;background:linear-gradient(90deg,rgba(20,30,50,.45),rgba(20,30,50,.1) 60%,rgba(0,0,0,0))}
.hero-title{top:238px;left:143px;font-size:66px;line-height:64px;color:var(--white)}
.hero-btn{top:477px;left:143px;width:287px;height:62px;font-size:14.5px}
.dots{top:435px;left:1127px;display:flex;flex-direction:column;gap:14px}
.dots span{width:9px;height:9px;border-radius:50%;background:var(--white);opacity:.8}
.hero-edge{top:660px;left:0}

/* about */
.about-art{top:865px;left:136px;width:438px;height:373px;background:linear-gradient(135deg,var(--orange) 0%,var(--amber) 40%,#3b4a8e 70%,var(--navy) 100%)}
.about-title{top:858px;left:611px;font-size:50px}
.about-text{top:940px;left:611px;width:450px;font-size:13.5px;line-height:27.3px;font-weight:300}
.about-btn{top:1180px;left:611px;width:153px;height:53px}

/* services */
.services{top:1346px;left:0}
.services-title{top:1515px;left:0;width:1136px;text-align:center;font-size:52px}
.service{position:absolute;top:1645px;width:200px;text-align:center}
.service-circle{width:160px;height:160px;border-radius:50%;margin:0 auto;display:flex;align-items:center;justify-content:center}
.service-label{margin-top:14px;font-family:"Exo 2",sans-serif;font-weight:600;font-size:18px;line-height:26px;color:var(--navy)}

/* publications */
.pubs-title{top:2155px;left:0;width:1200px;text-align:center;font-size:54px}
.card{position:absolute;top:2273px;width:289px}
.card-photo{height:186px}
.card-title{margin-top:30px;font-weight:600;font-size:17px;line-height:23px;color:var(--navy)}
.card-sub{margin-top:20px;font-size:12.5px;line-height:19px;color:var(--blue)}
.pubs-btn{top:2675px;left:486px;width:225px;height:54px}

/* contact */
.contact{top:2807px;left:0;width:1200px;height:760px;background:linear-gradient(180deg,#3a85cf 0%,#2f74b3 35%,#2a5f98 70%,#2f6aa8 100%)}
.contact-title{top:2900px;left:0;width:1200px;text-align:center;font-size:54px;color:var(--white)}
.field{position:absolute;background:var(--white);border-radius:2px;padding:16px 24px;font-size:14.5px;color:#8a8d99}
.submit{top:3284px;left:486px;width:225px;height:55px}
.contact-edge{top:3370px;left:0}
.footer-seal{top:3335px;left:317px;width:90px;height:90px;border-radius:50%;background:var(--white);display:flex;align-items:center;justify-content:center}
.footer-seal span{width:22px;height:22px;background:var(--orange)}

/* footer */
.foot-head{top:3562px;font-size:19px}
.quick{top:3610px;left:143px;list-style:none;font-size:13.5px;line-height:27.2px}
.info-row{position:absolute;left:400px;display:flex;align-items:center;gap:14px;font-size:13.5px;line-height:30px}
.info-icon{width:40px;height:40px;border-radius:50%;border:2px solid var(--blue);display:flex;align-items:center;justify-content:center;flex:none}
.badge{position:absolute;top:3570px;height:52px;border-radius:4px}
.foot-btn{top:3656px;left:687px;width:288px;height:53px;font-size:14px}
.rule{top:3804px;left:40px;width:1120px;height:1px;background:#e2e3ea}
.copy{top:3840px;left:0;width:1200px;text-align:center;font-size:13px;color:var(--text)}
</style>
</head>
<body>

<div class="abs top-rule"></div>
<header>
  <div class="abs brand"><span class="brand-mark"></span><span class="brand-name">HARVEST LEDGER PARTNERS</span></div>
  <div class="abs call">
    <svg width="40" height="40" viewBox="0 0 40 40"><circle cx="20" cy="20" r="18" fill="none" stroke="#f37122" stroke-width="2.5"/><path d="M14 11c1.5-1 3 0 3.5 1.5l1 3c.3 1-.2 1.8-1 2.3l-1 .6c.9 2.3 2.8 4.2 5 5l.7-1c.5-.8 1.4-1.2 2.3-.9l3 1c1.4.5 2.4 2 1.4 3.5-1.3 2-3.6 3-6 2-5-2-9-6-11-11-.8-2.4.3-4.7 2.1-6z" fill="#f37122"/></svg>
    CALL 555-014-2290
  </div>
  <nav class="abs nav">
    <a class="active" href="#">SELLER REPRESENTATION</a>
    <a href="#">BUSINESS VALUATIONS</a>
    <a href="#">DEPENDABLE ADVICE</a>
    <a href="#">INDUSTRY ARTICLES</a>
    <a href="#">INDUSTRY TRANSACTIONS</a>
    <a href="#">FAQ</a>
  </nav>
</header>

<section>
  <div class="abs hero" role="img" aria-label="Photo of a rental equipment yard with excavators and skid steer loaders behind a fence"></div>
  <div class="abs hero-shade"></div>
  <h1 class="abs heading hero-title">HARVEST<br>LEDGER<br>PARTNERS</h1>
  <a class="btn hero-btn" href="#">FREE CONFIDENTIAL CONVERSATION <svg class="btn-arrow" viewBox="0 0 16 16"><circle cx="8" cy="8" r="8" fill="#fff"/><path d="M6.5 4.5L10 8l-3.5 3.5" stroke="#f37122" stroke-width="2" fill="none"/></svg></a>
  <div class="abs dots"><span></span><span></span><span></span></div>
  <svg class="abs hero-edge" width="1200" height="176" viewBox="0 0 1200 176">
    <polygon points="0,163 350,8 1200,176 0,176" fill="#2a66ad"/>
    <polygon points="0,176 350,31 1200,176" fill="#fff"/>
  </svg>
</section>

<section>
  <div class="abs about-art" role="img" aria-label="Photo of an orange excavator and a scissor lift in a large decorative shape"></div>
  <h2 class="abs heading about-title">ABOUT US</h2>
  <p class="abs about-text">Gus Walloway, prior to Co-Founding Plum Corbel Group, LLC in July of 2011, was a Co-Founder of Walloway, Denholt &amp; Associates (WD&amp;A) in May of 2000. WD&amp;A was the leading Mergers &amp; Acquisitions firm in the equipment and party rental industry prior to its dissolution in June of 2011. Plum Corbel Group, LLC continues to have the success that Mr. Walloway spearheaded with WD&amp;A. Prior to owning his own firms, Mr. Walloway previously served as Vice-President, Corporate Development for a publicly traded national rental company.</p>
  <a class="btn about-btn" href="#">READ MORE <svg class="btn-arrow" viewBox="0 0 16 16"><circle cx="8" cy="8" r="8" fill="#fff"/><path d="M6.5 4.5L10 8l-3.5 3.5" stroke="#f37122" stroke-width="2" fill="none"/></svg></a>
</section>

<section>
  <svg class="abs services" width="1200" height="710" viewBox="0 0 1200 710">
    <defs>
      <linearGradient id="yard" x1="0" y1="0" x2="0" y2="1">
        <stop offset="0" stop-color="#fefbf7"/>
        <stop offset=".55" stop-color="#e6e4da"/>
        <stop offset=".8" stop-color="#d8cfa8"/>
        <stop offset="1" stop-color="#cbc6b8"/>
      </linearGradient>
    </defs>
    <path d="M0 0H800A355 355 0 0 1 800 710H0Z" fill="#ec5d1f"/>
    <path d="M0 76H800A278.5 278.5 0 0 1 800 633H0Z" fill="url(#yard)" role="img" aria-label="Faded photo of bulldozers parked under trees"/>
  </svg>
  <h2 class="abs heading services-title">OUR SERVICES</h2>

  <div class="service" style="left:123px">
    <div class="service-circle" style="background:var(--blue-deep)">
      <svg width="80" height="80" viewBox="0 0 80 80" fill="none" stroke="#fff" stroke-width="3" stroke-linecap="round" stroke-linejoin="round"><path d="M14 50l14-14 10 8 20-22"/><path d="M50 22h8v8"/><path d="M12 62h16l14-8c3-2 6 2 3 4l-10 7H20"/></svg>
    </div>
    <div class="service-label">Business Sale<br>Representation</div>
  </div>
  <div class="service" style="left:353px">
    <div class="service-circle" style="background:var(--yellow)">
      <svg width="84" height="70" viewBox="0 0 84 70" fill="none" stroke="#fff" stroke-width="3"><path d="M42 4l-10 12M42 4l10 12"/><rect x="6" y="16" width="72" height="48" rx="3"/><rect x="13" y="23" width="58" height="34"/><text x="42" y="48" fill="#fff" stroke="none" font-family="Rajdhani,sans-serif" font-weight="700" font-size="20" text-anchor="middle">RENT</text></svg>
    </div>
    <div class="service-label">Equipment<br>Rentals</div>
  </div>
  <div class="service" style="left:582px">
    <div class="service-circle" style="background:var(--sky)">
      <svg width="76" height="76" viewBox="0 0 76 76" fill="none" stroke="#fff" stroke-width="3" stroke-linejoin="round"><rect x="8" y="14" width="60" height="54" rx="3"/><path d="M8 28h60M22 8v12M54 8v12"/><path d="M38 34l4 8 8 1-6 5 2 8-8-4-8 4 2-8-6-5 8-1z"/></svg>
    </div>
    <div class="service-label">Special Event<br>Rentals</div>
  </div>
  <div class="service" style="left:812px">
    <div class="service-circle" style="background:var(--amber)">
      <svg width="72" height="80" viewBox="0 0 72 80" fill="none" stroke="#fff" stroke-width="2.5" stroke-linejoin="round"><path d="M20 8h32l10 10v54H20z"/><path d="M28 22h22M28 30h26M28 38h26M28 46h26"/><circle cx="16" cy="60" r="10"/><path d="M12 64v-4M16 64v-8M20 64v-6"/></svg>
    </div>
    <div class="service-label">Business<br>Valuations</div>
  </div>
</section>

<section>
  <h2 class="abs heading pubs-title">INDUSTRY PUBLICATIONS</h2>
  <article class="card" style="left:143px">
    <div class="card-photo" role="img" aria-label="Photo of boom lifts raised against a cloudy sky" style="background:linear-gradient(160deg,#c9d9e8,#7da3c7 50%,#2c4a6e)"></div>
    <div class="card-title">Rental Operator Quarterly,<br>June 2018 Cover Story By<br>Gus Walloway</div>
    <div class="card-sub">Transitioning Your Rental Business<br>-Cover Story</div>
  </article>
  <article class="card" style="left:456px">
    <div class="card-photo" role="img" aria-label="Photo of a showroom floor with material handling equipment" style="background:linear-gradient(160deg,#b7b2a7,#6e6a62 50%,#3d3a36)"></div>
    <div class="card-title">Lift Trade Wholesaler<br>Magazine August 2017: Cover<br>Story by Gus Walloway</div>
    <div class="card-sub">Cover Story: Rental Is About Profit, Not<br>Sales—by Gus Walloway</div>
  </article>
  <article class="card" style="left:768px">
    <div class="card-photo" role="img" aria-label="Photo of a golf course green with event tents and spectators" style="background:linear-gradient(180deg,#2f4a2c,#5c7d46 55%,#8fb068)"></div>
    <div class="card-title">Reach &amp; Access Journal<br>July/August 2015 Please<br>click link below</div>
    <div class="card-sub">Organization and Appearance Boost Business<br>Value—by Gus Walloway</div>
  </article>
  <a class="btn pubs-btn" href="#">VIEW MORE ARTICLES <svg class="btn-arrow" viewBox="0 0 16 16"><circle cx="8" cy="8" r="8" fill="#fff"/><path d="M6.5 4.5L10 8l-3.5 3.5" stroke="#f37122" stroke-width="2" fill="none"/></svg></a>
</section>

<section>
  <div class="abs contact" role="img" aria-label="Blue-tinted photo of a construction site with backhoe loaders"></div>
  <h2 class="abs heading contact-title">CONTACT FORM</h2>
  <div class="field" style="top:3007px;left:234px;width:359px;height:51px">First Name</div>
  <div class="field" style="top:3007px;left:605px;width:359px;height:51px">Last Name</div>
  <div class="field" style="top:3072px;left:234px;width:359px;height:51px">Email address</div>
  <div class="field" style="top:3072px;left:605px;width:359px;height:51px">Phone Number</div>
  <div class="field" style="top:3137px;left:234px;width:730px;height:113px">Message</div>
  <a class="btn submit" href="#">SUBMIT MESAGE <svg class="btn-arrow" viewBox="0 0 16 16"><circle cx="8" cy="8" r="8" fill="#fff"/><path d="M6.5 4.5L10 8l-3.5 3.5" stroke="#f37122" stroke-width="2" fill="none"/></svg></a>
  <svg class="abs contact-edge" width="1200" height="200" viewBox="0 0 1200 200">
    <polygon points="0,147 362,8 1200,180 1200,200 0,200" fill="#fff"/>
  </svg>
  <div class="abs footer-seal"><span></span></div>
</section>

<footer>
  <h3 class="abs heading foot-head" style="left:143px">QUICK LINKS</h3>
  <ul class="abs quick">
    <li>Seller Representation</li>
    <li>Business Valuations</li>
    <li>Dependable Advice</li>
    <li>Industry Articles</li>
    <li>Industry Transactions/News</li>
    <li>FAQ</li>
  </ul>
  <h3 class="abs heading foot-head" style="left:400px">CONTACT INFO</h3>
  <div class="info-row" style="top:3610px">
    <span class="info-icon"><svg width="16" height="20" viewBox="0 0 16 20"><path d="M8 1a6.5 6.5 0 0 0-6.5 6.5C1.5 12 8 19 8 19s6.5-7 6.5-11.5A6.5 6.5 0 0 0 8 1z" fill="none" stroke="#f37122" stroke-width="2"/><circle cx="8" cy="7.5" r="2.2" fill="#f37122"/></svg></span>
    <span>1187 Larkmoor Dr.<br>Fenwick Hollow, CA 95410</span>
  </div>
  <div class="info-row" style="top:3678px">
    <span class="info-icon"><svg width="20" height="14" viewBox="0 0 20 14"><rect x="1" y="1" width="18" height="12" rx="1.5" fill="#f37122"/><path d="M1.5 2l8.5 6 8.5-6" fill="none" stroke="#fff" stroke-width="1.5"/></svg></span>
    <span>Phone: 555-014-2290</span>
  </div>
  <div class="badge" style="left:694px;width:185px;background:#e8ecf5" role="img" aria-label="OTV associate member badge"></div>
  <div class="badge" style="left:920px;width:137px;background:#f4e6e4" role="img" aria-label="PLM proud associate member badge"></div>
  <a class="btn foot-btn" href="#">CALL GUS TODAY FOR A FREE <svg class="btn-arrow" viewBox="0 0 16 16"><circle cx="8" cy="8" r="8" fill="#fff"/><path d="M6.5 4.5L10 8l-3.5 3.5" stroke="#f37122" stroke-width="2" fill="none"/></svg></a>
  <div class="abs rule"></div>
  <p class="abs copy">© 2021 Harvest Ledger Partners. All rights reserved &nbsp;|&nbsp; Privacy &nbsp;|&nbsp; Terms of Use</p>
</footer>

</body>
</html>
```